New Business Card Design Project

Need a design that will create an impact / strong impression towards our clients for our business. We are in the lighting business and we do lighting retrofits for large commercial to industrial clientele.

Target Market(s)

Lighting Industry

Industry/Entity Type

Business

Font styles to use
Other font styles liked:
• we would like to use the font on our logo, not sure what it is though..

Requirements
Must have
• Our logo.
Nice to have
• We are open to suggestions that have to do with lighting.

```html
<!DOCTYPE html>
<html lang="en">
<head>
<meta charset="utf-8">
<title>Brightway Retrofit Co. — Business Card</title>
<link href="https://fonts.googleapis.com/css2?family=Montserrat:wght@600;700&family=PT+Sans:wght@400&display=swap" rel="stylesheet">
<style>
  :root {
    --stage: #232323;
    --paper: #ffffff;
    --green-deep: #1c8a36;
    --green-mid: #3aa646;
    --green-light: #6cc955;
    --green-ink: #1f7a2e;
    --logo-ink: #1e6a2c;
    --text-dark: #222222;
    --white: #ffffff;
  }
  * { margin: 0; padding: 0; box-sizing: border-box; }
  html, body { width: 1200px; height: 900px; overflow: hidden; }
  body { background: var(--stage); position: relative; font-family: "PT Sans", sans-serif; }

  .card { position: absolute; width: 440px; height: 271px; overflow: hidden; }
  .card--front { left: 149px; top: 306px; background: var(--paper); }
  .card--back {
    left: 608px; top: 306px; height: 272px;
    background: linear-gradient(135deg, var(--green-deep) 0%, var(--green-light) 42%, var(--green-mid) 70%, var(--green-deep) 100%);
  }

  .brand { position: absolute; display: flex; align-items: center; gap: 8px;
    font-family: "Montserrat", sans-serif; font-weight: 700; letter-spacing: 1px; }
  .brand__mark { width: 14px; height: 14px; }
  .card--front .brand { left: 22px; top: 122px; font-size: 22px; color: var(--logo-ink); }
  .card--front .brand__mark { background: var(--logo-ink); }
  .card--back .brand { left: 0; right: 0; top: 120px; justify-content: center; font-size: 26px; color: var(--white); }
  .card--back .brand__mark { background: var(--white); }

  .divider { position: absolute; left: 231px; top: 75px; width: 2px; height: 121px; background: var(--green-mid); }

  .contact { position: absolute; left: 248px; top: 71px; color: var(--text-dark); }
  .contact__name { font-family: "Montserrat", sans-serif; font-weight: 700; font-size: 15.5px; color: var(--green-ink); line-height: 18px; }
  .contact__role { font-size: 12.5px; line-height: 15px; }
  .contact__list { list-style: none; margin-top: 9px; font-size: 12.5px; line-height: 16px; }
  .contact__list li { display: flex; align-items: center; gap: 6px; }
  .contact__list svg { width: 9px; height: 9px; fill: var(--green-ink); flex: none; }
  .contact__address { margin-top: 7px; font-size: 12.5px; line-height: 15.5px; }

  .back-url { position: absolute; left: 0; right: 0; top: 229px; text-align: center; color: var(--white); font-size: 13px; }
</style>
</head>
<body>
  <section class="card card--front">
    <div class="brand"><span class="brand__mark"></span>BRIGHTWAY</div>
    <div class="divider"></div>
    <div class="contact">
      <p class="contact__name">JONATHAN SMITH</p>
      <p class="contact__role">Managing Director</p>
      <ul class="contact__list">
        <li><svg viewBox="0 0 10 10"><path d="M2 0.5l2 2-1 1.2c.6 1.3 1.6 2.3 2.9 2.9l1.2-1 2 2-1.2 1.6C4.5 9.2 0.8 5.5.4 1.7z"/></svg>(044)123456789</li>
        <li><svg viewBox="0 0 10 10"><path d="M0 2h10v6H0z M0 2l5 3.5L10 2" stroke="#fff" stroke-width=".8"/></svg>info@youremail.com</li>
        <li><svg viewBox="0 0 10 10"><circle cx="5" cy="5" r="5"/><path d="M0 5h10M5 0c-2 2.5-2 7.5 0 10M5 0c2 2.5 2 7.5 0 10" stroke="#fff" stroke-width=".6" fill="none"/></svg>www.websitename.com</li>
      </ul>
      <p class="contact__address">1234, Address GoesHere,<br>Country name, 12345</p>
    </div>
  </section>

  <section class="card card--back">
    <div class="brand"><span class="brand__mark"></span>BRIGHTWAY</div>
    <p class="back-url">www.webname.com</p>
  </section>
</body>
</html>
```